Website Update for Global Company - Solar Technology - Brisqell

We recently released our first version of our website kelvaris.com. However despite a longer process of developing the page, it is still missing the elements of a brilliant website. (Currently it looks dead and boring) We are having problems integrating our logo and want to create a more catching site. The task involves an updated and without changing most of main elements in the existing page. (Unless you can do it even better) The blue color needs to be kept but can be changed within the blue-spectrum. The logo text (KELVARIS) must be better integrated in the site, however the main logo could be used in elements like we have tried with the background. The surface of the logo could be changed to 3D or metallic, or any other theme that would make the site more complete.
It would be good if some elements of the site could be used on business cards and invoices to keep the company identity.
Kelvaris is a new development company specialized in green energy and sustainable development. We do design, engineering, manufacturing, sourcing and other processes related to product development – both as consultants and for own products.
Keep the look of the site as professional as possible, and with a cooperate-looking style.

Link to existing page: www.kelvaris.com

Brief Update : After reviewing the designs we would like all new and current designers to make more bold designs that stands out from the rest. We do not like the standard layout that looks like any other cooperate homepage. We want a very unique and very lively page - with faded images and effects when hoovering like seen on our existing page. Try make all elements blend together, and use faded background images instead of just white color - or something else.

Make the site unique !

Industry/Entity Type

Solar Energy

Contact Information for Business Card

Owner/Founder/CEO : Frederik Lysgaard Holm
Company name: Kelvaris ApS
Email: frederik.lysgaard@kelvaris.dk
Phone: +45 71 83 96 54
Slogan Sustainable Development
Address: Havnestien 18, 2
DK-5820 Svendborg, Denmark

Number of Pages Required

3 page

Font styles to use
Serif
Sans Serif

Colors
0555a3
85acd3
cedeed
3176b5
cee9f5
85cae6
0293ce
86cfc6
33b8a4

```html
<!DOCTYPE html>
<html lang="en">
<head>
<meta charset="utf-8">
<title>Kelvaris – Sustainable Solutions</title>
<link href="https://fonts.googleapis.com/css2?family=Open+Sans:wght@400;600;700&family=Lato:wght@300;400;700&display=swap" rel="stylesheet">
<style>
:root{
  --blue-deep:#0555a3;
  --blue-mid:#3176b5;
  --blue-soft:#85acd3;
  --blue-pale:#cedeed;
  --sky:#0293ce;
  --sky-soft:#85cae6;
  --sky-pale:#cee9f5;
  --teal:#33b8a4;
  --green:#7dbb3a;
  --ink:#2d3440;
  --grey:#6c7480;
  --footer:#0b3f7c;
  --footer-dark:#072f5e;
}
*{box-sizing:border-box;margin:0;padding:0}
html,body{width:1200px;height:2280px;overflow:hidden}
body{font-family:"Open Sans",Arial,sans-serif;color:var(--ink);background:#fff;position:relative}

/* header */
.site-header{position:absolute;top:0;left:0;width:1200px;height:72px;background:#fff}
.brand{position:absolute;left:88px;top:18px;font-family:"Lato",sans-serif;font-weight:700;font-size:30px;line-height:36px;color:var(--blue-deep)}
.top-phone{position:absolute;right:88px;top:10px;font-size:13px;color:var(--ink);display:flex;align-items:center;gap:6px}
.main-nav{position:absolute;right:88px;top:40px;display:flex;gap:4px}
.main-nav a{font-family:"Lato",sans-serif;font-size:11px;font-weight:700;color:var(--blue-deep);text-decoration:none;padding:4px 8px;letter-spacing:.5px;border:1px solid transparent}
.main-nav a.active{border-color:var(--sky);color:var(--sky)}

/* hero */
.hero{position:absolute;top:72px;left:0;width:1200px;height:600px;
  background:radial-gradient(ellipse at 30% 60%,#f3b25a 0%,#c0703a 18%,#3a4b63 55%,#1a2738 100%)}
.hero-arrow{position:absolute;top:290px}
.hero-caption{position:absolute;left:0;right:0;top:548px;text-align:center;font-family:"Lato",sans-serif;font-size:22px;color:#fff;letter-spacing:.3px}
.hero-band{position:absolute;left:0;right:0;top:536px;height:52px;background:linear-gradient(90deg,rgba(10,20,35,0),rgba(10,20,35,.55) 30%,rgba(10,20,35,.55) 70%,rgba(10,20,35,0))}

/* section titles */
.section-title{font-family:"Lato",sans-serif;font-size:28px;font-weight:700;text-align:center;letter-spacing:.5px}
.section-title .accent{color:var(--blue-deep)}
.title-rule{display:flex;align-items:center;justify-content:center;gap:8px;margin-top:6px}
.title-rule span{width:60px;height:1px;background:var(--blue-soft)}
.title-rule i{width:8px;height:8px;background:var(--blue-mid);border-radius:50%}

/* services */
.services{position:absolute;top:672px;left:0;width:1200px;height:288px;background:linear-gradient(#fff,#f4f8fc)}
.services .section-title{margin-top:28px}
.service-row{position:absolute;top:94px;left:140px;width:920px;display:flex;justify-content:space-between}
.service{width:150px;text-align:center}
.service-icon{width:56px;height:56px;border-radius:50%;background:var(--blue-deep);margin:0 auto;display:flex;align-items:center;justify-content:center;box-shadow:0 0 0 4px var(--blue-pale)}
.service h3{font-family:"Lato",sans-serif;font-size:14px;font-weight:700;margin:12px 0 6px}
.service p{font-size:9.5px;line-height:14px;color:var(--grey)}
.btn-small{display:inline-block;margin-top:8px;font-size:9px;color:var(--blue-mid);border:1px solid var(--blue-soft);padding:2px 10px;border-radius:2px}
.svc-arrow{position:absolute;top:118px}

/* welcome */
.welcome{position:absolute;top:960px;left:0;width:1200px;height:500px;
  background:linear-gradient(180deg,var(--sky-soft) 0%,#a9d6ec 55%,var(--sky-pale) 100%)}
.welcome-title{position:absolute;top:40px;left:0;right:0;text-align:center;font-family:"Lato",sans-serif;font-size:28px;color:#fff;font-weight:700}
.welcome-title .light{font-weight:300}
.welcome-text{position:absolute;top:96px;left:140px;width:920px;text-align:center;color:#fff;font-size:11px;line-height:18px}
.info-card{position:absolute;top:204px;width:292px;height:230px;background:#fff;text-align:center;padding-top:52px;box-shadow:0 2px 6px rgba(5,85,163,.15)}
.info-card .badge{position:absolute;left:116px;top:-30px;width:60px;height:60px;border-radius:50%;background:var(--blue-deep);border:4px solid #fff;display:flex;align-items:center;justify-content:center}
.info-card h3{font-family:"Lato",sans-serif;font-size:24px;color:var(--blue-deep);font-weight:700}
.info-card p{font-size:10px;line-height:15px;color:var(--grey);padding:10px 26px 0}

/* reviews */
.reviews{position:absolute;top:1460px;left:0;width:1200px;height:360px;
  background:linear-gradient(160deg,#5a6a72 0%,#3f4f58 45%,#6d7b78 100%)}
.reviews-title{position:absolute;top:28px;left:0;right:0;text-align:center;font-family:"Lato",sans-serif;font-size:32px;color:#fff}
.reviews-sub{position:absolute;top:74px;left:0;right:0;text-align:center;color:#e6edf2;font-size:11px}
.quote-box{position:absolute;top:116px;left:160px;width:880px;height:120px;background:rgba(255,255,255,.82);padding:24px 130px 0 56px;font-size:10.5px;line-height:17px;color:var(--ink)}
.quote-mark{position:absolute;left:18px;top:8px;font-family:Georgia,serif;font-size:48px;color:var(--blue-mid)}
.reviewer-photo{position:absolute;left:938px;top:124px;width:72px;height:72px;border-radius:50%;background:linear-gradient(#b9c4cc,#7f8c96);border:3px solid #fff}
.reviewer-name{position:absolute;top:246px;right:170px;color:#fff;font-size:11px}
.dots{position:absolute;top:246px;left:168px;display:flex;gap:6px}
.dots i{width:6px;height:6px;border-radius:50%;background:#fff;opacity:.6}
.dots i.on{opacity:1}

/* clients */
.clients{position:absolute;top:1820px;left:0;width:1200px;height:110px;background:linear-gradient(90deg,#dfe9f3,#f3f7fb)}
.clients-title{position:absolute;left:160px;top:22px;font-family:"Lato",sans-serif;font-size:28px;line-height:32px;color:var(--ink);font-weight:400}
.client-row{position:absolute;left:360px;top:40px;width:700px;display:flex;justify-content:space-between;align-items:center}
.client{display:flex;align-items:center;gap:6px;font-family:"Lato",sans-serif;font-weight:700;font-size:20px;color:#3a4656}
.client i{width:14px;height:14px;background:#3a4656}

/* newsletter */
.newsletter{position:absolute;top:1930px;left:0;width:1200px;height:56px;background:linear-gradient(90deg,var(--blue-mid),var(--blue-deep))}
.newsletter h4{position:absolute;left:212px;top:18px;font-family:"Lato",sans-serif;font-weight:400;font-size:16px;color:#fff}
.nl-input{position:absolute;left:560px;top:15px;width:300px;height:26px;background:#fff;font-size:10px;color:#9aa3ad;padding:6px 10px}
.nl-btn{position:absolute;left:866px;top:15px;width:100px;height:26px;background:var(--green);color:#fff;font-size:12px;text-align:center;line-height:26px}

/* footer */
.site-footer{position:absolute;top:1986px;left:0;width:1200px;height:254px;background:var(--footer);color:#d6e3f1}
.footer-col{position:absolute;top:28px}
.footer-col h5{font-family:"Lato",sans-serif;font-size:14px;color:#fff;font-weight:700;margin-bottom:12px}
.footer-col li{list-style:none;font-size:10.5px;line-height:22px;display:flex;align-items:center;gap:8px}
.footer-col li::before{content:"›";color:var(--sky-soft)}
.footer-col.contact li::before,.footer-col.social li::before{content:none}
.ico{width:18px;height:18px;border-radius:50%;background:var(--blue-mid);display:inline-flex;align-items:center;justify-content:center;flex:none}
.sq{width:18px;height:18px;background:var(--sky);flex:none}
.map{width:200px;height:130px;background:linear-gradient(135deg,#e9eef2,#c9d6df)}
.copyright{position:absolute;top:2240px;left:0;width:1200px;height:40px;background:var(--footer-dark);color:#a9bdd3;font-size:10px;text-align:center;line-height:40px}
</style>
</head>
<body>

<header class="site-header">
  <div class="brand">Kelvaris</div>
  <div class="top-phone">
    <svg width="14" height="14" viewBox="0 0 24 24"><path fill="#0555a3" d="M6.6 10.8a15.1 15.1 0 0 0 6.6 6.6l2.2-2.2c.3-.3.7-.4 1-.2 1.1.4 2.3.6 3.6.6.6 0 1 .4 1 1V20c0 .6-.4 1-1 1A17 17 0 0 1 3 4c0-.6.4-1 1-1h3.5c.6 0 1 .4 1 1 0 1.3.2 2.5.6 3.6.1.3 0 .7-.2 1z"/></svg>
    +45 71 83 96 54
  </div>
  <nav class="main-nav">
    <a class="active" href="#">HOME</a><a href="#">WORK</a><a href="#">EXPERTISE</a><a href="#">APPROACH</a><a href="#">CLIENTS</a><a href="#">ABOUT</a><a href="#">CONTACT</a>
  </nav>
</header>

<section class="hero" role="img" aria-label="Photo of a welder at work with bright sparks flying">
  <svg class="hero-arrow" style="left:24px" width="24" height="40" viewBox="0 0 24 40"><path d="M20 4 4 20l16 16" stroke="#fff" stroke-width="4" fill="none"/></svg>
  <svg class="hero-arrow" style="right:24px" width="24" height="40" viewBox="0 0 24 40"><path d="m4 4 16 16L4 36" stroke="#fff" stroke-width="4" fill="none"/></svg>
  <div class="hero-band"></div>
  <p class="hero-caption">We Provide Complete Services Throughout The Product Development Process</p>
</section>

<section class="services">
  <h2 class="section-title">OUR <span class="accent">SERVICES</span></h2>
  <div class="title-rule"><span></span><i></i><span></span></div>
  <svg class="svc-arrow" style="left:80px" width="12" height="20" viewBox="0 0 12 20"><path d="M10 2 2 10l8 8" stroke="#2d3440" stroke-width="2.5" fill="none"/></svg>
  <svg class="svc-arrow" style="right:80px" width="12" height="20" viewBox="0 0 12 20"><path d="m2 2 8 8-8 8" stroke="#2d3440" stroke-width="2.5" fill="none"/></svg>
  <div class="service-row">
    <div class="service">
      <div class="service-icon"><svg width="26" height="26" viewBox="0 0 24 24"><path fill="#fff" d="M3 17.3V21h3.7L17.8 9.9l-3.7-3.7zM20.7 7a1 1 0 0 0 0-1.4l-2.3-2.3a1 1 0 0 0-1.4 0l-1.8 1.8 3.7 3.7z"/></svg></div>
      <h3>Design</h3>
      <p>Ideas shaped into clear concepts and drawings ready for the next step of work.</p>
      <span class="btn-small">Read More</span>
    </div>
    <div class="service">
      <div class="service-icon"><svg width="28" height="28" viewBox="0 0 24 24"><circle cx="12" cy="12" r="3.5" fill="none" stroke="#fff" stroke-width="2"/><path stroke="#fff" stroke-width="2.4" d="M12 2v4M12 18v4M2 12h4M18 12h4M5 5l2.8 2.8M16.2 16.2 19 19M5 19l2.8-2.8M16.2 7.8 19 5"/></svg></div>
      <h3>Engineering</h3>
      <p>Solid technical work that turns each concept into a product that truly performs.</p>
      <span class="btn-small">Read More</span>
    </div>
    <div class="service">
      <div class="service-icon"><svg width="28" height="28" viewBox="0 0 24 24"><path fill="#fff" d="M2 21V10l6 4v-4l6 4V4h4l1 10h3v7z"/></svg></div>
      <h3>Manufacturing</h3>
      <p>Reliable production partners and methods that keep quality high and costs low.</p>
      <span class="btn-small">Read More</span>
    </div>
    <div class="service">
      <div class="service-icon"><svg width="28" height="28" viewBox="0 0 24 24"><circle cx="12" cy="12" r="9" fill="none" stroke="#fff" stroke-width="2"/><path d="M3 12h18M12 3c3 3 3 15 0 18M12 3c-3 3-3 15 0 18" stroke="#fff" stroke-width="1.6" fill="none"/></svg></div>
      <h3>Sourcing</h3>
      <p>Trusted suppliers found worldwide so every part arrives on time and to spec.</p>
      <span class="btn-small">Read More</span>
    </div>
    <div class="service">
      <div class="service-icon"><svg width="28" height="28" viewBox="0 0 24 24"><circle cx="12" cy="12" r="9" fill="none" stroke="#fff" stroke-width="2"/><circle cx="12" cy="12" r="5" fill="none" stroke="#fff" stroke-width="2"/><circle cx="12" cy="12" r="1.6" fill="#fff"/></svg></div>
      <h3>Other Processes</h3>
      <p>Support through testing, launch and the many other steps of development.</p>
      <span class="btn-small">Read More</span>
    </div>
  </div>
</section>

<section class="welcome" role="img" aria-label="Faded photo of a green landscape behind the welcome section">
  <h2 class="welcome-title">WELCOME TO KELVARIS <span class="light">SUSTAINABLE SOLUTIONS</span></h2>
  <p class="welcome-text">We are a new development company working in green energy and sustainable growth. From first idea to finished product we help our partners design, engineer, build and source solutions, both as consultants and for our own products, with care for people and the planet at every step of the way.</p>
  <div class="info-card" style="left:288px">
    <div class="badge"><svg width="28" height="28" viewBox="0 0 24 24"><circle cx="8" cy="8" r="3" fill="#fff"/><circle cx="16" cy="8" r="3" fill="#fff"/><path fill="#fff" d="M2 19c0-3.5 2.7-6 6-6s6 2.5 6 6zM12 19c0-2.2.8-4 2-5 .6-.3 1.3-.5 2-.5 3.3 0 6 2.5 6 5.5z"/></svg></div>
    <h3>Who We Are</h3>
    <p>A small team of engineers and designers with a shared drive to build clean, lasting energy products for a greener future.</p>
    <span class="btn-small">Read More</span>
  </div>
  <div class="info-card" style="left:620px">
    <div class="badge"><svg width="28" height="28" viewBox="0 0 24 24"><circle cx="12" cy="12" r="9" fill="none" stroke="#fff" stroke-width="2"/><circle cx="12" cy="12" r="5" fill="none" stroke="#fff" stroke-width="2"/><circle cx="12" cy="12" r="1.6" fill="#fff"/></svg></div>
    <h3>Our Vision</h3>
    <p>To make sustainable technology simple to build and easy to use, so every new product helps lower our shared impact.</p>
    <span class="btn-small">Read More</span>
  </div>
</section>

<section class="reviews" role="img" aria-label="Faded photo of raised thumbs up behind the customer reviews">
  <h2 class="reviews-title">Our Customer Reviews</h2>
  <p class="reviews-sub">Read what our partners say about working with us on their products and projects.</p>
  <div class="quote-box">
    <span class="quote-mark">“</span>
    Working with the team was a real pleasure from start to finish. They listened closely, gave clear advice and delivered a product that met every goal we set. Their knowledge of sustainable design and sourcing saved us both time and money, and we look forward to our next project together.
  </div>
  <div class="reviewer-photo" role="img" aria-label="Portrait of the reviewer"></div>
  <p class="reviewer-name">Henrik Dalby, CEO</p>
  <div class="dots"><i class="on"></i><i></i><i></i></div>
</section>

<section class="clients">
  <h2 class="clients-title">Our<br>Clients</h2>
  <div class="client-row">
    <span class="client"><i></i>Phasewell</span>
    <span class="client">Archvale</span>
    <span class="client"><i></i>Centrova</span>
    <span class="client">Arkmont</span>
    <span class="client"><i></i>Soltrix</span>
  </div>
</section>

<section class="newsletter">
  <h4>Subscribe to Our Newsletter</h4>
  <div class="nl-input">Enter your email</div>
  <div class="nl-btn">Subscribe</div>
</section>

<footer class="site-footer">
  <div class="footer-col" style="left:88px">
    <h5>Quick Links</h5>
    <ul><li>Home</li><li>Work</li><li>Expertise</li><li>Approach</li><li>Clients</li><li>About</li><li>Contact</li></ul>
  </div>
  <div class="footer-col contact" style="left:330px">
    <h5>Contact Us</h5>
    <ul>
      <li><span class="ico"><svg width="10" height="10" viewBox="0 0 24 24"><path fill="#fff" d="M12 2a7 7 0 0 0-7 7c0 5 7 13 7 13s7-8 7-13a7 7 0 0 0-7-7zm0 9.5A2.5 2.5 0 1 1 12 6.5a2.5 2.5 0 0 1 0 5z"/></svg></span>Kelvaris ApS, Havnestien 18, 2</li>
      <li><span class="ico" style="visibility:hidden"></span>DK-5820 Svendborg, Denmark</li>
      <li><span class="ico"><svg width="10" height="10" viewBox="0 0 24 24"><path fill="#fff" d="M6.6 10.8a15.1 15.1 0 0 0 6.6 6.6l2.2-2.2c.3-.3.7-.4 1-.2 1.1.4 2.3.6 3.6.6.6 0 1 .4 1 1V20c0 .6-.4 1-1 1A17 17 0 0 1 3 4c0-.6.4-1 1-1h3.5c.6 0 1 .4 1 1 0 1.3.2 2.5.6 3.6.1.3 0 .7-.2 1z"/></svg></span>+45 71 83 96 54</li>
      <li><span class="ico"><svg width="10" height="10" viewBox="0 0 24 24"><path fill="#fff" d="M2 5h20v14H2zm2 2v.5l8 5 8-5V7z"/></svg></span>frederik.lysgaard@kelvaris.dk</li>
      <li><span class="ico"><svg width="10" height="10" viewBox="0 0 24 24"><circle cx="12" cy="12" r="9" fill="none" stroke="#fff" stroke-width="2.5"/></svg></span>www.kelvaris.com</li>
    </ul>
  </div>
  <div class="footer-col" style="left:640px">
    <h5>Location Map</h5>
    <div class="map" role="img" aria-label="Street map showing the office location"></div>
  </div>
  <div class="footer-col social" style="left:930px">
    <h5>Follow Us</h5>
    <ul><li><span class="sq"></span>Circlebook</li><li><span class="sq"></span>Chirper</li><li><span class="sq"></span>Searchly</li><li><span class="sq"></span>Workwire</li></ul>
  </div>
</footer>
<div class="copyright">Copyright © 2015 Kelvaris. All Rights Reserved.</div>

</body>
</html>
```